Maple Glow Label

Design a label for new brand called Maple Glow. The specific product label :
Maple Glow Cocoa Butter Lotion. You only need to design the front label.
I have included the logo and a bottle jpeg with 2 bottles on it. Please try your best.

Requirements
Must have
• text on the label other than the logo:
cocoa butter
lotion
8.5oz/250ml

Original Moisturizing Formula
Smoothes Marks
Protect Skin

__________________________________
- ALTERNATIVE TEXT TO ALSO USE:
Smoothes Dry Skin, Blemishes & Stretch Marks
Softens Hands, Face and Body
Vitamin E

```html
<!DOCTYPE html>
<html lang="en">
<head>
<meta charset="utf-8">
<title>Maple Glow Cocoa Butter Lotion – Front Label</title>
<link href="https://fonts.googleapis.com/css2?family=Montserrat:wght@600;700&family=Arimo:wght@400&display=swap" rel="stylesheet">
<style>
  :root {
    --page-bg: #eef1f0;
    --label-white: #fbfbfa;
    --cream-shade: #e7e3dc;
    --cream-light: #ffffff;
    --olive: #3f4a2a;
    --ink: #2b2b2b;
    --brand-pink: #d3206f;
    --gold: #c9a66b;
    --gold-light: #ecd9b0;
    --rule: #b8ad98;
    --skin-tone: #e9c7b4;
    --skin-shadow: #c99a86;
  }
  html, body {
    margin: 0;
    padding: 0;
    width: 960px;
    height: 1200px;
    overflow: hidden;
    background: var(--page-bg);
  }
  .canvas {
    position: relative;
    width: 960px;
    height: 1200px;
  }
  .label {
    position: absolute;
    left: 100px;
    top: 60px;
    width: 760px;
    height: 1080px;
    border-radius: 28px;
    overflow: hidden;
    background: var(--label-white);
    box-shadow: 0 2px 14px rgba(0,0,0,0.08);
  }
  .label__satin {
    position: absolute;
    inset: 0;
    background:
      radial-gradient(ellipse 70% 30% at 80% 18%, var(--cream-light) 0%, rgba(255,255,255,0) 70%),
      linear-gradient(160deg, var(--cream-shade) 0%, var(--cream-light) 22%, var(--cream-shade) 38%, var(--cream-light) 52%, #efece6 70%, var(--cream-light) 100%);
  }
  .label__content {
    position: relative;
    text-align: center;
    padding-top: 150px;
  }
  .brand-name {
    font-family: "Montserrat", sans-serif;
    font-weight: 700;
    font-size: 54px;
    color: var(--brand-pink);
    letter-spacing: 0;
    margin: 0 0 44px;
  }
  .product-title {
    font-family: "Montserrat", sans-serif;
    font-weight: 700;
    font-size: 74px;
    line-height: 1.02;
    color: var(--olive);
    margin: 0;
    text-transform: uppercase;
  }
  .formula {
    font-family: "Arimo", sans-serif;
    font-size: 26px;
    line-height: 1.1;
    letter-spacing: 5px;
    color: var(--ink);
    text-transform: uppercase;
    margin: 16px 0 0;
  }
  .claim {
    font-family: "Arimo", sans-serif;
    font-size: 30px;
    color: var(--ink);
    margin: 8px 0 0;
  }
  .portrait {
    width: 224px;
    height: 224px;
    margin: 42px auto 0;
    border-radius: 50%;
    padding: 9px;
    box-sizing: border-box;
    background: linear-gradient(140deg, var(--gold-light), var(--gold) 45%, var(--gold-light) 80%);
  }
  .portrait__fill {
    width: 100%;
    height: 100%;
    border-radius: 50%;
    border: 4px solid #fff;
    box-sizing: border-box;
    background: radial-gradient(circle at 45% 45%, var(--skin-tone) 0%, #f3ded2 55%, var(--skin-shadow) 100%);
  }
  .benefits {
    list-style: none;
    padding: 0;
    margin: 90px auto 0;
    width: 380px;
    font-family: "Arimo", sans-serif;
    font-size: 22px;
    color: var(--ink);
  }
  .benefits li {
    padding: 7px 0 6px;
    border-bottom: 2px solid var(--rule);
  }
  .benefits li:last-child {
    border-bottom: none;
  }
  .net-size {
    position: absolute;
    right: 70px;
    bottom: 56px;
    font-family: "Arimo", sans-serif;
    font-size: 19px;
    color: var(--ink);
  }
</style>
</head>
<body>
<div class="canvas">
  <section class="label">
    <div class="label__satin" role="img" aria-label="Silky white cream swirl background"></div>
    <div class="label__content">
      <p class="brand-name">Maple Glow</p>
      <h1 class="product-title">Cocoa Butter<br>Lotion</h1>
      <p class="formula">Original<br>Moisturizing Formula</p>
      <p class="claim">Smoothes Marks &amp; Protect Skin</p>
      <div class="portrait">
        <div class="portrait__fill" role="img" aria-label="Photo of a woman applying lotion to her cheek"></div>
      </div>
      <ul class="benefits">
        <li>Smoothes Dry Skin</li>
        <li>Blemishes &amp; Stretch Marks</li>
        <li>Softens Hands, Face and Body</li>
        <li>Vitamin E</li>
      </ul>
    </div>
    <p class="net-size">8.5oz (250 ml)</p>
  </section>
</div>
</body>
</html>
```